Professional & attention grabbing.

A business card design, front and back. I already have a logo I will attach, but I am open to something new as well.
Things to include:
Name:
Title:
Phone:
Email:
Wanting something that is professional but attention grabbing.
Also we do a lot of work using drones on natural gas pipelines (leading the future)if you want to include any of that. I'm open to ideas.
Target Market(s)
Natural gas transmission industry / greenhouse gas mitigation industry
Industry/Entity Type
Business
Contact Information for Business Card
All details have been conveyed above.
Colors
Designer to choose colors to be used in the design.
Look and feel
Each slider illustrates characteristics of the customer's brand and the style your logo design should communicate.

```html
<!DOCTYPE html>
<html lang="en">
<head>
<meta charset="utf-8">
<title>Orvane Inspections – Business Card</title>
<link href="https://fonts.googleapis.com/css2?family=Open+Sans:wght@400;600;700&display=swap" rel="stylesheet">
<style>
  :root {
    --backdrop: #5a4231;
    --brand-red: #be2026;
    --brand-black: #1e1e1e;
    --ink-white: #ffffff;
  }
  * { margin: 0; padding: 0; box-sizing: border-box; }
  html, body { width: 1200px; height: 1000px; overflow: hidden; }
  body {
    background: var(--backdrop);
    font-family: "Open Sans", Arial, sans-serif;
    color: var(--ink-white);
    position: relative;
  }
  .card {
    position: absolute;
    left: 266px;
    width: 666px;
    height: 397px;
    overflow: hidden;
    box-shadow: 0 4px 12px rgba(0,0,0,0.35);
  }
  .card--front { top: 74px; background: var(--brand-red); }
  .card--back { top: 534px; background: var(--brand-black); }

  .front-band { position: absolute; right: 0; top: 0; width: 320px; height: 397px; }

  .wordmark { position: absolute; display: flex; align-items: center; }
  .wordmark__square { background: var(--ink-white); flex: none; }
  .wordmark__name {
    font-weight: 700;
    color: var(--ink-white);
    text-transform: uppercase;
    line-height: 1.05;
  }
  .card--front .wordmark { left: 32px; top: 31px; gap: 18px; }
  .card--front .wordmark__square { width: 108px; height: 108px; }
  .card--front .wordmark__name { font-size: 34px; }

  .card--back .wordmark { left: 129px; top: 123px; gap: 30px; }
  .card--back .wordmark__square { width: 148px; height: 148px; background: var(--brand-red); }
  .card--back .wordmark__name { font-size: 44px; }

  .person { position: absolute; left: 33px; top: 186px; }
  .person__name { font-size: 21px; font-weight: 600; text-transform: uppercase; letter-spacing: 0.3px; line-height: 1.2; }
  .person__title { font-size: 16px; line-height: 1.3; }

  .address { position: absolute; left: 33px; top: 252px; font-size: 16px; line-height: 20px; font-style: normal; }

  .contacts { position: absolute; left: 33px; top: 302px; list-style: none; font-size: 16px; }
  .contacts li { display: flex; align-items: center; gap: 8px; height: 23.5px; }
  .contacts svg { width: 14px; height: 14px; fill: var(--ink-white); flex: none; }
</style>
</head>
<body>

<section class="card card--front" aria-label="Card front">
  <svg class="front-band" viewBox="0 0 320 397" aria-hidden="true">
    <path d="M320 0 H250 C230 90 90 150 60 260 C40 330 80 397 120 397 H320 Z" fill="var(--brand-black)"/>
  </svg>

  <div class="wordmark">
    <span class="wordmark__square"></span>
    <span class="wordmark__name">Orvane<br>Inspections</span>
  </div>

  <div class="person">
    <p class="person__name">Dorian Pell</p>
    <p class="person__title">Managing Director</p>
  </div>

  <address class="address">1480 Alder Creek Road<br>Hagerstown, MD 21740</address>

  <ul class="contacts">
    <li>
      <svg viewBox="0 0 24 24"><path d="M6.6 10.8a15 15 0 0 0 6.6 6.6l2.2-2.2c.3-.3.7-.4 1-.2 1.1.4 2.3.6 3.6.6.6 0 1 .4 1 1V20c0 .6-.4 1-1 1A17 17 0 0 1 3 4c0-.6.4-1 1-1h3.5c.6 0 1 .4 1 1 0 1.3.2 2.5.6 3.6.1.3 0 .7-.2 1z"/></svg>
      <span>+ 000 000 0000</span>
    </li>
    <li>
      <svg viewBox="0 0 24 24"><path d="M2 5h20v14H2z M2 5l10 8 10-8" fill="none" stroke="#fff" stroke-width="2"/></svg>
      <span>info@orvane-inspect.com</span>
    </li>
    <li>
      <svg viewBox="0 0 24 24"><circle cx="12" cy="12" r="9" fill="none" stroke="#fff" stroke-width="2"/><path d="M3 12h18M12 3c3 3 3 15 0 18M12 3c-3 3-3 15 0 18" fill="none" stroke="#fff" stroke-width="1.6"/></svg>
      <span>www.orvane-inspect.com</span>
    </li>
  </ul>
</section>

<section class="card card--back" aria-label="Card back">
  <div class="wordmark">
    <span class="wordmark__square"></span>
    <span class="wordmark__name">Orvane<br>Inspections</span>
  </div>
</section>

</body>
</html>
```